New Software Development Firm Needs Business Cards!

We just completed a successful logo design project on MakerHive and need to develop a business card design using that shiny new logo. We want a clean, modern design that communicates professionalism and tech savvy without being cliche'.

The company is "Bramble Logic, LLC", but our dba is "Bramble" The business card address should reflect the full company name in the address. The logo just uses "Bramble".

Photoshop or Illustrator source files will be required, along with exact font name(s) and source(s) used.

The design will need to work well with our letterhead as well. I'm also launching a project right now for letterhead and envelopes as well. Please submit to both projects! We're excited to see the designs. Thanks...

Target Market(s)

Small to medium business professionals

Industry/Entity Type

Business

Requirements
Must have
• Need place for:
- Company name and address (5 lines)
- Phone: (1 number)
- Fax: (1 number)
- Employee's name
- Employee's position
- Employee's email address
- Company web site URL
Nice to have
• Probably want a white card, but we're open to options.

```html
<!DOCTYPE html>
<html lang="en">
<head>
<meta charset="utf-8">
<title>Bramble — Business Card</title>
<link rel="stylesheet" href="https://fonts.googleapis.com/css2?family=Lato:ital,wght@0,300;0,400;0,700;1,400&display=swap">
<style>
  :root {
    --backdrop: #d9d9d9;
    --card-dark: #262626;
    --card-light: #f7f7f7;
    --ink: #1e1e1e;
    --accent: #d3121b;
    --logo-white: #f4f4f4;
  }
  * { box-sizing: border-box; margin: 0; padding: 0; }
  html, body {
    width: 1200px; height: 900px; overflow: hidden;
    background: var(--backdrop);
    font-family: "Lato", Arial, sans-serif;
    color: var(--ink);
  }
  .sheet {
    width: 1200px; height: 900px;
    display: flex; flex-direction: column;
    align-items: center; justify-content: center; gap: 50px;
  }
  .card {
    position: relative;
    width: 660px; height: 377px;
    box-shadow: 0 6px 18px rgba(0,0,0,0.22);
    overflow: hidden;
  }
  /* Front */
  .card-front { background: var(--card-dark); }
  .card-front .accent-line { position: absolute; inset: 0; }
  .brand-name {
    position: absolute; right: 44px; bottom: 60px;
    font-size: 86px; font-weight: 400; letter-spacing: 2px;
    color: var(--logo-white); line-height: 1;
  }
  /* Back */
  .card-back { background: var(--card-light); padding: 54px 56px; }
  .person { display: flex; align-items: baseline; gap: 12px; }
  .person-mark {
    width: 14px; height: 14px; background: var(--accent);
    align-self: center;
  }
  .person-name { font-size: 29px; font-weight: 400; }
  .person-role { font-size: 18px; text-transform: uppercase; letter-spacing: 0.5px; }
  .person-role::before { content: "| "; font-size: 15px; }
  .email { margin: 4px 0 0 26px; font-size: 16px; }
  .phones {
    display: grid; grid-template-columns: 48px auto;
    margin: 32px 0 0 0; font-size: 18px; line-height: 1.2;
  }
  .phones dt { color: var(--accent); font-style: italic; text-align: right; padding-right: 14px; font-size: 16px; }
  .phones dd { font-style: italic; }
  .address {
    margin: 36px 0 0 22px; font-style: italic;
    font-size: 18px; line-height: 1.3;
  }
  .website {
    position: absolute; right: 56px; bottom: 40px; font-size: 18px;
  }
</style>
</head>
<body>
  <main class="sheet">
    <section class="card card-front" aria-label="Card front">
      <svg class="accent-line" width="660" height="377" viewBox="0 0 660 377" aria-hidden="true">
        <line x1="190" y1="105" x2="660" y2="205" stroke="var(--accent)" stroke-width="1.5"/>
      </svg>
      <div class="brand-name">Bramble</div>
    </section>

    <section class="card card-back" aria-label="Card back">
      <div class="person">
        <span class="person-mark" aria-hidden="true"></span>
        <span class="person-name">Tomas Reyna</span>
        <span class="person-role">Manager</span>
      </div>
      <p class="email">tomas.reyna@bramble.com</p>
      <dl class="phones">
        <dt>tel</dt><dd>(55) 5550 2170</dd>
        <dt>fax</dt><dd>(55) 5550 2170</dd>
      </dl>
      <address class="address">
        Bramble LLC<br>
        Alameda 14. Col. Roma<br>
        The City DF 06700. MX.<br>
        12345 The Country
      </address>
      <p class="website">www.bramble.com</p>
    </section>
  </main>
</body>
</html>
```